Brightpath Strategic Advisers F.Z.E
Professional
Khalid Yousef Nasser
Founder & CEO
Corvana Trade Park
info@bsa-qx.com
www.bsa-qx.com
Training & Consultancy on:
QBXR Assessment & Training
Leadership Development & Coaching
Change Management
Strategy Management
Performance Management
Quality & Process Management
TQM
HR Development
HR Procedures & Regulation
Logo & Full Stationeries & P.P Presentation first page and continues sheet & Proposal document cover & continues sheet

```html
<!DOCTYPE html>
<html lang="en">
<head>
<meta charset="utf-8">
<title>Brightpath Strategic Advisers – Business Card</title>
<link rel="stylesheet" href="https://fonts.googleapis.com/css2?family=Arimo:wght@400;700&family=Roboto+Condensed:wght@700&display=swap">
<style>
  :root {
    --backdrop: #e4e4e2;
    --card: #ffffff;
    --ink: #2b2b2b;
    --ink-soft: #555555;
    --orange: #f7941d;
    --orange-deep: #ef6a10;
    --orange-light: #fbb040;
    --black: #1c1c1c;
    --grey-line: #c9c9c9;
  }
  * { margin: 0; padding: 0; box-sizing: border-box; }
  html, body { width: 1200px; height: 906px; overflow: hidden; }
  body {
    background: var(--backdrop);
    font-family: "Arimo", Arial, sans-serif;
    color: var(--ink);
    position: relative;
  }
  .card {
    position: absolute;
    background: var(--card);
    border-radius: 22px;
    overflow: hidden;
    box-shadow: 0 6px 18px rgba(0,0,0,0.18);
  }
  .card-front { left: 43px; top: 36px; width: 574px; height: 367px; }
  .card-back  { left: 439px; top: 468px; width: 711px; height: 401px; }

  .card-art { position: absolute; inset: 0; width: 100%; height: 100%; }

  .brand {
    position: absolute;
    display: flex;
    align-items: center;
    gap: 12px;
  }
  .brand-dot {
    width: 22px; height: 22px;
    border-radius: 50%;
    background: var(--orange);
    flex: none;
  }
  .brand-name {
    font-family: "Roboto Condensed", "Arial Narrow", sans-serif;
    font-weight: 700;
    color: var(--ink);
    text-transform: uppercase;
    line-height: 1.05;
    letter-spacing: 0.2px;
  }
  .card-front .brand { left: 34px; top: 58px; }
  .card-front .brand-name { font-size: 27px; }

  .holder { position: absolute; left: 34px; top: 186px; }
  .holder-name {
    font-size: 21px;
    font-weight: 700;
    color: var(--ink);
    padding-bottom: 6px;
    border-bottom: 1.5px solid var(--grey-line);
    width: 300px;
  }
  .holder-role { font-size: 13px; color: var(--ink-soft); margin-top: 9px; }

  .contact {
    position: absolute;
    left: 404px; top: 255px;
    color: #ffffff;
    font-size: 15px;
    line-height: 22px;
  }
  .contact .web { margin-top: 14px; }

  .services {
    position: absolute;
    left: 40px; top: 26px;
    list-style: none;
  }
  .services li {
    display: flex;
    align-items: center;
    height: 31px;
    font-size: 13px;
    font-weight: 700;
    color: var(--ink);
  }
  .services li::before {
    content: "";
    width: 40px;
    height: 2px;
    margin-right: 14px;
    background: linear-gradient(90deg, rgba(247,148,29,0), var(--orange));
  }
  .services li.services-heading { font-weight: 700; }

  .card-back .brand { right: 30px; bottom: 52px; }
  .card-back .brand-name { font-size: 25px; }
</style>
</head>
<body>

<section class="card card-front" aria-label="Business card front">
  <svg class="card-art" viewBox="0 0 574 367" preserveAspectRatio="none" aria-hidden="true">
    <defs>
      <linearGradient id="orange-sweep" x1="0" y1="0" x2="1" y2="0">
        <stop offset="0" stop-color="var(--orange-light)"/>
        <stop offset="1" stop-color="var(--orange-deep)"/>
      </linearGradient>
    </defs>
    <path d="M0 335 C 160 325 390 255 574 138 L574 367 L0 367 Z" fill="url(#orange-sweep)"/>
    <path d="M0 300 C 170 292 400 222 574 98 L574 120 C 400 240 170 310 0 320 Z" fill="var(--black)"/>
    <path d="M0 288 C 180 280 400 212 574 86 L574 92 C 400 220 180 286 0 293 Z" fill="#bdbdbd"/>
    <path d="M0 330 C 160 322 390 250 574 132 L574 138 C 390 258 160 328 0 337 Z" fill="#ffffff" opacity="0.7"/>
  </svg>

  <div class="brand">
    <span class="brand-dot"></span>
    <span class="brand-name">Brightpath Strategic<br>Advisers F.Z.E</span>
  </div>

  <div class="holder">
    <p class="holder-name">Khalid Yousef Nasser</p>
    <p class="holder-role">Founder &amp; CEO</p>
  </div>

  <div class="contact">
    <p>Corvana Trade Park</p>
    <p>P:00971555018274</p>
    <p>E: info@bsa-qx.com</p>
    <p class="web">www.bsa-qx.com</p>
  </div>
</section>

<section class="card card-back" aria-label="Business card back">
  <ul class="services">
    <li class="services-heading">Training &amp; Consultancy on:</li>
    <li>QBXR Assessment &amp; Training</li>
    <li>Leadership Development &amp; Coaching</li>
    <li>Change Management</li>
    <li>Strategy Management</li>
    <li>Performance Management</li>
    <li>Quality &amp; Process Management</li>
    <li>TQM</li>
    <li>HR Development</li>
    <li>HR Procedures &amp; Regulation</li>
  </ul>

  <div class="brand">
    <span class="brand-dot"></span>
    <span class="brand-name">Brightpath Strategic<br>Advisers F.Z.E</span>
  </div>
</section>

</body>
</html>
```